Website Design for A Leading Live Casino Software Provider

We provide live casino software to other land based and online gaming establishments. We are a B2B provider.

```html
<!DOCTYPE html>
<html lang="en">
<head>
<meta charset="utf-8">
<title>Meridian Play Labs – Live Casino Software</title>
<link href="https://fonts.googleapis.com/css2?family=Arimo:wght@400;700&family=Roboto:wght@300;400&family=Roboto+Condensed:wght@700&family=Open+Sans:wght@400&display=swap" rel="stylesheet">
<style>
:root{
  --ink:#1b1b1b;
  --text:#333;
  --muted:#8a8a8a;
  --blue:#1a8fd0;
  --blue-dark:#0d6ea8;
  --blue-light:#35b0ea;
  --page:#eeeeee;
  --frame:#8c8c8c;
  --footer:#222222;
  --footer-text:#6f6f6f;
}
*{margin:0;padding:0;box-sizing:border-box}
html,body{width:1200px;height:1036px;overflow:hidden}
body{position:relative;background:var(--page);font-family:"Arimo",Arial,sans-serif;color:var(--text)}
.abs{position:absolute}
.top-strip{left:0;top:0;width:1200px;height:17px;background:#1c1c1c}
.header{left:0;top:17px;width:1200px;height:80px;background:#fff}
.brand{left:227px;top:37px;display:flex;align-items:center;gap:8px;white-space:nowrap}
.brand-dot{width:30px;height:30px;border-radius:50%;background:var(--blue);flex:none}
.brand-name{font-family:"Arimo",Arial,sans-serif;font-weight:700;font-size:16px;color:var(--ink);letter-spacing:.3px}
.nav-icons{left:455px;top:27px;width:530px;height:40px}
.nav-bar{left:433px;top:73px;width:555px;height:25px;background:linear-gradient(#3a3a3a,#0f0f0f);border-radius:8px 8px 0 0}
.nav{left:433px;top:73px;width:555px;height:25px;display:flex;list-style:none}
.nav li{flex:1;text-align:center;font-family:"Roboto Condensed","Arial Narrow",sans-serif;font-weight:700;font-size:12.5px;line-height:25px;color:#fff;white-space:nowrap}
.nav li.active{background:linear-gradient(var(--blue-light),var(--blue-dark))}
.blue-band{left:0;top:97px;width:1200px;height:38px;background:linear-gradient(#2aa2df,#0f76b8)}
.hero-shadow{left:240px;top:396px;width:720px;height:26px;border-radius:50%;background:radial-gradient(ellipse at center,rgba(0,0,0,.35),rgba(0,0,0,0) 70%)}
.hero{left:212px;top:136px;width:776px;height:270px;background:var(--frame);padding:9px}
.hero-photo{width:100%;height:100%;background:linear-gradient(135deg,#2b2620 0%,#5a4a3a 35%,#8a7058 55%,#2c2724 100%)}
.hero-caption{left:213px;top:311px;width:408px;height:75px;background:rgba(25,140,205,.82);border-radius:0 14px 14px 0;padding:15px 0 0 40px;color:#fff}
.hero-caption h2{font-family:"Roboto",Arial,sans-serif;font-weight:300;font-size:25px;line-height:28px}
.hero-caption p{font-size:9px;margin-top:2px;white-space:nowrap}
.section-title{font-family:"Roboto",Arial,sans-serif;font-weight:400;font-size:20px;color:var(--ink);white-space:nowrap}
.dealers-title{left:244px;top:462px}
.carousel{left:228px;top:488px;width:312px;height:168px}
.slide{position:absolute;background:linear-gradient(#8a6a58,#3a4c6a);box-shadow:0 2px 3px rgba(0,0,0,.25)}
.slide.reflect{opacity:.25}
.carousel-badge{position:absolute;left:134px;top:118px;width:56px;height:18px;background:#e2e2e2;font-size:6px;line-height:8px;text-align:center;color:#555;padding-top:1px}
.carousel-arrow{position:absolute;top:140px;width:12px;height:14px}
.dealers-note{left:228px;top:663px;width:312px;text-align:center;font-size:8.5px;color:#222;white-space:nowrap}
.about-title{left:592px;top:448px;font-family:"Roboto",Arial,sans-serif;font-weight:300;font-size:40px;color:var(--ink);letter-spacing:-.5px}
.about-copy{left:593px;top:494px;width:372px;font-family:"Open Sans",Verdana,sans-serif;font-size:10.6px;line-height:14.5px;color:#333}
.about-copy p+p{margin-top:14.5px}
.news-title{left:244px;top:723px}
.news-list{left:243px;top:772px;width:730px;height:60px;list-style:none}
.news-list li{position:absolute;display:flex;align-items:center;gap:10px;font-weight:700;font-size:10px;color:#333;white-space:nowrap}
.tick{width:16px;height:16px}
.footer{left:0;top:855px;width:1200px;height:181px;background:var(--footer)}
.footer-cta{left:244px;top:883px;font-family:"Roboto",Arial,sans-serif;font-weight:400;font-size:19.5px;color:#fff;white-space:nowrap}
.footer-copy{left:240px;top:937px;width:725px;font-size:8.5px;line-height:19.5px;color:var(--footer-text)}
.footer-rule{left:212px;top:1001px;width:776px;height:1px;background:#3a3a3a}
.footer-legal{left:212px;top:1011px;font-size:10px;color:#a0a0a0;white-space:nowrap}
.footer-legal b{color:#fff;font-weight:700}
</style>
</head>
<body>
<div class="abs top-strip"></div>
<header class="abs header"></header>
<div class="abs brand"><span class="brand-dot"></span><span class="brand-name">MERIDIAN PLAY LABS</span></div>

<svg class="abs nav-icons" viewBox="0 0 530 40" aria-hidden="true">
  <g transform="translate(14,6)"><path d="M0 13 L14 1 L28 13 Z" fill="#c0392b"/><rect x="4" y="13" width="20" height="15" fill="#e8d7b8"/><rect x="11" y="18" width="6" height="10" fill="#8a5a2b"/></g>
  <g transform="translate(96,6)"><rect x="0" y="4" width="16" height="16" rx="3" fill="#c62828" transform="rotate(-15 8 12)"/><rect x="8" y="12" width="16" height="16" rx="3" fill="#e53935"/><circle cx="16" cy="20" r="2" fill="#fff"/></g>
  <g transform="translate(166,10)"><rect x="0" y="4" width="32" height="20" rx="2" fill="#8d5a2b"/><rect x="2" y="6" width="28" height="8" fill="#e0a040"/><rect x="12" y="0" width="8" height="5" fill="#5a3a1a"/></g>
  <g transform="translate(252,6)"><circle cx="14" cy="14" r="13" fill="#555"/><circle cx="14" cy="14" r="10" fill="#ddd"/><circle cx="14" cy="14" r="3" fill="#555"/><circle cx="14" cy="7" r="2.5" fill="#555"/><circle cx="14" cy="21" r="2.5" fill="#555"/><circle cx="7" cy="14" r="2.5" fill="#555"/><circle cx="21" cy="14" r="2.5" fill="#555"/></g>
  <g transform="translate(318,6)"><rect x="0" y="3" width="24" height="24" rx="2" fill="#fff" stroke="#bbb"/><rect x="0" y="3" width="24" height="7" fill="#d32f2f"/><rect x="4" y="14" width="16" height="2" fill="#ccc"/><rect x="4" y="19" width="12" height="2" fill="#ccc"/></g>
  <g transform="translate(394,8)"><rect x="0" y="0" width="30" height="24" rx="2" fill="#fff" stroke="#7a9a5a"/><rect x="3" y="4" width="10" height="10" fill="#5a8ac8"/><rect x="16" y="5" width="11" height="2" fill="#7a9a5a"/><rect x="16" y="10" width="11" height="2" fill="#7a9a5a"/><rect x="3" y="17" width="24" height="2" fill="#7a9a5a"/></g>
  <g transform="translate(470,8)"><path d="M0 8 L8 8 L24 0 L24 24 L8 16 L0 16 Z" fill="#e64a19"/><rect x="3" y="16" width="5" height="8" fill="#bf360c"/></g>
</svg>
<div class="abs nav-bar"></div>
<ul class="abs nav">
  <li class="active">Home</li><li>Live Game</li><li>Solutions</li><li>Videos</li><li>News &amp; Events</li><li>About Us</li><li>Contact Us</li>
</ul>
<div class="abs blue-band"></div>

<div class="abs hero-shadow"></div>
<div class="abs hero"><div class="hero-photo" role="img" aria-label="Photo of three men in tuxedos cheering at a casino"></div></div>
<div class="abs hero-caption">
  <h2>Stay Ahead of the Competition</h2>
  <p>We Deliver Cutting Edge Technology to the Most Advanced Companies in the Industry</p>
</div>

<h3 class="abs section-title dealers-title">Get To Know our Beautiful Dealers</h3>
<div class="abs carousel">
  <div class="slide" style="left:0;top:34px;width:38px;height:32px" role="img" aria-label="Casino dealer photo"></div>
  <div class="slide" style="left:68px;top:2px;width:38px;height:30px" role="img" aria-label="Casino table photo"></div>
  <div class="slide" style="left:27px;top:52px;width:70px;height:58px" role="img" aria-label="Live dealer photo"></div>
  <div class="slide reflect" style="left:27px;top:112px;width:70px;height:22px"></div>
  <div class="slide" style="left:134px;top:50px;width:56px;height:66px;background:linear-gradient(#c9c9c9,#7a4a3a)" role="img" aria-label="Roulette wheel photo"></div>
  <div class="carousel-badge">Download the new<br>3D Carousel!</div>
  <div class="slide" style="left:180px;top:18px;width:38px;height:28px" role="img" aria-label="Card game photo"></div>
  <div class="slide" style="left:232px;top:48px;width:48px;height:50px" role="img" aria-label="Casino lights photo"></div>
  <div class="slide" style="left:250px;top:30px;width:40px;height:22px" role="img" aria-label="Casino photo"></div>
  <div class="slide reflect" style="left:232px;top:100px;width:48px;height:20px"></div>
  <svg class="carousel-arrow" style="left:56px" viewBox="0 0 12 14" aria-hidden="true"><path d="M9 1 L3 7 L9 13" stroke="#555" stroke-width="2" fill="none"/></svg>
  <svg class="carousel-arrow" style="left:236px" viewBox="0 0 12 14" aria-hidden="true"><path d="M3 1 L9 7 L3 13" stroke="#555" stroke-width="2" fill="none"/></svg>
</div>
<p class="abs dealers-note">They Will Ensure Your Players are Smiling Even when Losing!</p>

<h1 class="abs about-title">About Us</h1>
<div class="abs about-copy">
  <p>We are Meridian Play Labs S.A. The preeminent providers of Live Interactive Streaming Games of Skill and Chance.</p>
  <p>The Online Gaming Industry has come a long way in the last decade. In today's very competitive market you must provide your customers with new and unique gaming venues. That's where we come in.</p>
  <p>Our suite of Live Interactive Games adds value to your existing gaming environments with no erosion of profit from your other established revenue sources. Our products are great Affiliate Drivers ... LIve Interactive Gaming from MPL is your profit force multiplier!</p>
  <p>We invite you peruse our demonstration videos and make contact with us for a personal evaluation of how MPL's gaming software can be put to work for you.</p>
</div>

<h3 class="abs section-title news-title">Latest News &amp; Events</h3>
<ul class="abs news-list">
  <li style="left:0;top:0"><svg class="tick" viewBox="0 0 16 16"><circle cx="8" cy="8" r="8" fill="var(--blue)"/><path d="M4 8 L7 11 L12 5" stroke="#fff" stroke-width="2" fill="none"/></svg>Lorem ipsum dolor sit amet,</li>
  <li style="left:235px;top:0"><svg class="tick" viewBox="0 0 16 16"><circle cx="8" cy="8" r="8" fill="var(--blue)"/><path d="M4 8 L7 11 L12 5" stroke="#fff" stroke-width="2" fill="none"/></svg>Lorem ipsum dolor sit amet,</li>
  <li style="left:477px;top:0"><svg class="tick" viewBox="0 0 16 16"><circle cx="8" cy="8" r="8" fill="var(--blue)"/><path d="M4 8 L7 11 L12 5" stroke="#fff" stroke-width="2" fill="none"/></svg>Lorem ipsum dolor sit amet,</li>
  <li style="left:0;top:39px"><svg class="tick" viewBox="0 0 16 16"><circle cx="8" cy="8" r="8" fill="var(--blue)"/><path d="M4 8 L7 11 L12 5" stroke="#fff" stroke-width="2" fill="none"/></svg>Lorem ipsum dolor sit amet,</li>
  <li style="left:235px;top:39px"><svg class="tick" viewBox="0 0 16 16"><circle cx="8" cy="8" r="8" fill="var(--blue)"/><path d="M4 8 L7 11 L12 5" stroke="#fff" stroke-width="2" fill="none"/></svg>Lorem ipsum dolor sit amet,</li>
</ul>

<footer class="abs footer"></footer>
<p class="abs footer-cta">Call Toll Free 1-xxx-xxx-xxxx and get a FREE Demo of our Software and Solutions</p>
<p class="abs footer-copy">Meridian Play Labs is a leader among online casino software providers. Our team of expert internet casino software developers, managers and marketers are here to ensure that any project you need, is a project Meridian Play Labs can deliver. Our Casino services and consulting solutions can take your business to the next level. Our online casino software licensing can help any start up achieve the quickest and most secure return on investment.</p>
<div class="abs footer-rule"></div>
<p class="abs footer-legal">© Copyright <b>mplaylabs.com</b>. All Rights Reserved</p>
</body>
</html>
```